One of a kind, 100% Pure & Natural Skincare line needs stunning product label

We need product label design for new natural skincare company called Milo & Tess Skincare. We create luxurious, 100% pure & natural skincare that is free from ingredients that may be potentially irritating to the skin. No toxins, preservatives or additives. Our initial product is Harbor Glow Balm, a nourishing face cream that suits discerning women with mature skin and those with dry/sensitive skin needing extra hydration. Also those that choose to minimize their exposure to environmental toxins. Our brand is simple yet elegant, supporting a holistic, authentic lifestyle and embracing natural skincare.

Target Market(s)

Discerning women with mature skin and those with dry/sensitive skin needing extra hydration. Also those that choose to minimize their exposure to environmental toxins.

Industry/Entity Type

Skin Care Product

Font styles to use
Sans Serif
Script

Colors
f9d9e8
fef1ee

Requirements
Must have
• The Logo.
HARBOR GLOW BALM
EMBRACING NATURAL SKINCARE
Labels must be feminine, simple/minimal yet stylish. Uncluttered yet elegant.
This is a very natural product with minimal ingredients.
Nice to have
• The logo can be incorporated in to the label, or It can be left separate as a sticker on top of the jar. The product is a firm balm consistency and is in frosted glass jars with matt silver lids.
Jar height is 45mm, width is 60mm.
Label height: 28mm and length 185mm
Should not have
• Natural or farmers market type theme. No Bold/loud lettering.

```html
<!DOCTYPE html>
<html lang="en">
<head>
<meta charset="utf-8">
<title>Harbor Glow Balm – Label Options</title>
<link rel="stylesheet" href="https://fonts.googleapis.com/css2?family=Marcellus&family=Open+Sans:wght@400;600&family=Satisfy&display=swap">
<style>
  :root {
    --stage: #c4c4c4;
    --paper: #ffffff;
    --blush: #fdf0f0;
    --orchid: #d292c4;
    --cocoa: #8b4c48;
    --ink: #2b2b2b;
    --logo-dot: #f2b8c6;
  }
  * { box-sizing: border-box; margin: 0; padding: 0; }
  html, body { width: 1074px; height: 1200px; overflow: hidden; }
  body {
    background: var(--stage);
    font-family: "Open Sans", sans-serif;
    color: var(--ink);
    position: relative;
  }
  .label {
    position: absolute;
    left: 61px;
    width: 951px;
    height: 146px;
    background: var(--paper);
    overflow: hidden;
  }
  .label--pill { top: 345px; }
  .label--slant { top: 527px; background: var(--paper); }
  .label--plain { top: 709px; }

  /* shapes */
  .pill {
    position: absolute;
    top: 25px;
    height: 102px;
    background: var(--blush);
  }
  .pill--left { left: 0; width: 298px; border-radius: 0 51px 51px 0; }
  .pill--right { right: 0; width: 299px; border-radius: 51px 0 0 51px; }
  .slant-shapes { position: absolute; inset: 0; width: 951px; height: 146px; }
  .slant-shapes polygon { fill: var(--blush); }

  /* centre brand block */
  .brand {
    position: absolute;
    left: 0; right: 0; top: 10px;
    text-align: center;
  }
  .brand-mark {
    display: inline-flex;
    align-items: center;
    gap: 4px;
    font-family: "Open Sans", sans-serif;
    font-size: 8px;
    color: var(--ink);
    height: 22px;
  }
  .brand-mark .dot {
    width: 9px; height: 9px; border-radius: 50%;
    background: var(--logo-dot);
  }
  .product-name {
    font-family: "Marcellus", sans-serif;
    color: var(--orchid);
    font-size: 31px;
    line-height: 33px;
    letter-spacing: 1px;
    font-weight: 400;
  }
  .tagline {
    font-family: "Satisfy", cursive;
    color: var(--cocoa);
    font-size: 17px;
    line-height: 20px;
    margin-top: -1px;
  }

  /* info blocks */
  .info {
    position: absolute;
    font-size: 9.3px;
    line-height: 11px;
  }
  .info p + p, .info h3 + p { margin: 0; }
  .info h3 { font-size: 9.3px; font-weight: 400; }
  .info .gap { margin-top: 9px; }
  .info .store { font-weight: 600; margin-top: 7px; }
  .centered { text-align: center; }
  .made {
    position: absolute;
    font-size: 8.8px;
    line-height: 11px;
  }
  .made strong { font-weight: 600; display: block; }
  .made span { font-size: 7px; }
  .batch {
    position: absolute;
    display: flex;
    align-items: center;
    gap: 7px;
    font-size: 15px;
    font-weight: 400;
  }
  .batch svg { width: 18px; height: 20px; }
</style>
</head>
<body>

<!-- Option 1: rounded panels -->
<section class="label label--pill" aria-label="Label option with rounded panels">
  <div class="pill pill--left"></div>
  <div class="pill pill--right"></div>
  <div class="info centered" style="left:20px; width:256px; top:34px;">
    <h3>Ingredients:</h3>
    <p>tallow from pasture raised goats, frankincense, sandalwood &amp; myrrh essential oils.</p>
    <h3 class="gap">Directions:</h3>
    <p>Soften small amount in palm of hand &amp; gently massage into skin as often as required.</p>
    <p class="store">Store below 25°C</p>
  </div>
  <div class="brand">
    <div class="brand-mark"><i class="dot"></i>Milo &amp; Tess</div>
    <h1 class="product-name">HARBOR<br>GLOW BALM</h1>
    <p class="tagline">Embracing Natural Skincare</p>
  </div>
  <div class="info centered" style="left:682px; width:256px; top:34px;">
    <h3>Caution:</h3>
    <p>Keep out of reach of children. If pregnant or breastfeeding, consult your healthcare practitioner. Avoid contact with eyes &amp; sensitive areas. Allergy patch test recommended. If irritation occurs, discontinue use.</p>
  </div>
  <div class="made" style="left:703px; top:98px;"><strong>MADE IN AUSTRALIA</strong><span>info@milotessskincare.com.au</span></div>
  <div class="batch" style="left:882px; top:99px;">B#
    <svg viewBox="0 0 18 20" aria-label="6 months after opening"><path d="M3 4 L14 1 L15 3 L4 6 Z" fill="none" stroke="#444" stroke-width=".9"/><rect x="2" y="8" width="14" height="11" rx="1.5" fill="none" stroke="#444" stroke-width=".9"/><text x="9" y="17" font-size="5.5" text-anchor="middle" font-family="Open Sans, sans-serif" fill="#444">6M</text></svg>
  </div>
</section>

<!-- Option 2: slanted panels -->
<section class="label label--slant" aria-label="Label option with slanted panels">
  <svg class="slant-shapes" viewBox="0 0 951 146" aria-hidden="true">
    <polygon points="0,0 306,0 342,146 0,146"/>
    <polygon points="314,0 322,0 362,146 352,146"/>
    <polygon points="951,0 645,0 609,146 951,146"/>
    <polygon points="637,0 629,0 589,146 599,146"/>
  </svg>
  <div class="info" style="left:29px; width:210px; top:28px;">
    <h3>Ingredients:</h3>
    <p>tallow from pasture raised goats, frankincense, sandalwood &amp; myrrh essential oils.</p>
    <h3 class="gap">Directions:</h3>
    <p>Soften small amount in palm of hand &amp; gently massage into skin as often as required.</p>
    <p class="store">Store below 25°C</p>
  </div>
  <div class="brand">
    <div class="brand-mark"><i class="dot"></i>Milo &amp; Tess</div>
    <h1 class="product-name">HARBOR<br>GLOW BALM</h1>
    <p class="tagline">Embracing Natural Skincare</p>
  </div>
  <div class="info" style="left:719px; width:215px; top:28px;">
    <h3>Caution:</h3>
    <p>Keep out of reach of children. If pregnant or breastfeeding, consult your healthcare practitioner. Avoid contact with eyes &amp; sensitive areas. Allergy patch test recommended. If irritation occurs, discontinue use.</p>
  </div>
  <div class="made" style="left:719px; top:110px;"><strong>MADE IN AUSTRALIA</strong><span>info@milotessskincare.com.au</span></div>
  <div class="batch" style="left:882px; top:111px;">B#
    <svg viewBox="0 0 18 20" aria-label="6 months after opening"><path d="M3 4 L14 1 L15 3 L4 6 Z" fill="none" stroke="#444" stroke-width=".9"/><rect x="2" y="8" width="14" height="11" rx="1.5" fill="none" stroke="#444" stroke-width=".9"/><text x="9" y="17" font-size="5.5" text-anchor="middle" font-family="Open Sans, sans-serif" fill="#444">6M</text></svg>
  </div>
</section>

<!-- Option 3: plain white -->
<section class="label label--plain" aria-label="Plain white label option">
  <div class="info centered" style="left:92px; width:210px; top:28px;">
    <h3>Ingredients:</h3>
    <p>tallow from pasture raised goats, frankincense, sandalwood &amp; myrrh essential oils.</p>
    <h3 class="gap">Directions:</h3>
    <p>Soften small amount in palm of hand &amp; gently massage into skin as often as required.</p>
    <p class="store">Store below 25°C</p>
  </div>
  <div class="brand" style="left:12px;">
    <div class="brand-mark"><i class="dot"></i>Milo &amp; Tess</div>
    <h1 class="product-name">HARBOR<br>GLOW BALM</h1>
    <p class="tagline">Embracing Natural Skincare</p>
  </div>
  <div class="info centered" style="left:782px; width:215px; top:28px; transform:translateX(-108px);">
    <h3>Caution:</h3>
    <p>Keep out of reach of children. If pregnant or breastfeeding, consult your healthcare practitioner. Avoid contact with eyes &amp; sensitive areas. Allergy patch test recommended. If irritation occurs, discontinue use.</p>
  </div>
  <div class="made" style="left:726px; top:110px;"><strong>MADE IN AUSTRALIA</strong><span>info@milotessskincare.com.au</span></div>
  <div class="batch" style="left:888px; top:111px;">B#
    <svg viewBox="0 0 18 20" aria-label="6 months after opening"><path d="M3 4 L14 1 L15 3 L4 6 Z" fill="none" stroke="#444" stroke-width=".9"/><rect x="2" y="8" width="14" height="11" rx="1.5" fill="none" stroke="#444" stroke-width=".9"/><text x="9" y="17" font-size="5.5" text-anchor="middle" font-family="Open Sans, sans-serif" fill="#444">6M</text></svg>
  </div>
</section>

</body>
</html>
```